Harbor Kestrel
Your Trusted Advisors
Professional
Rosalind Okafor
Partner
418 Tamarack Lane
Ashford Falls, OR 97402
rosalind.okafor@harborkestrel.co
www.harborkestrel.co

```html
<!DOCTYPE html>
<html lang="en">
<head>
<meta charset="utf-8">
<title>Harbor Kestrel – Business Cards</title>
<link rel="stylesheet" href="https://fonts.googleapis.com/css2?family=Open+Sans:wght@400;600;700;800&display=swap">
<style>
  :root {
    --brand-red: #d0202e;
    --brand-dark: #2b2b2b;
    --card-white: #ffffff;
    --curve-grey: #bdbdbd;
    --backdrop: #ecebe8;
    --text-light: #ffffff;
  }
  * { margin: 0; padding: 0; box-sizing: border-box; }
  html, body { width: 1200px; height: 833px; overflow: hidden; }
  body {
    background: var(--backdrop);
    font-family: "Open Sans", Arial, sans-serif;
    position: relative;
  }
  .card {
    position: absolute;
    border-radius: 20px;
    overflow: hidden;
    box-shadow: 0 4px 14px rgba(0,0,0,0.18);
  }
  .card-front {
    left: 432px; top: 96px;
    width: 540px; height: 420px;
    background: var(--brand-red);
    color: var(--text-light);
  }
  .card-front .white-swoop { position: absolute; inset: 0; }
  .brand-name {
    position: absolute;
    display: flex; align-items: center; gap: 8px;
    font-weight: 800;
    color: var(--brand-dark);
    letter-spacing: 0.3px;
    white-space: nowrap;
  }
  .brand-dot {
    display: inline-block;
    border-radius: 50%;
    background: var(--brand-red);
    flex: none;
  }
  .card-front .brand-name {
    left: 22px; top: 126px;
    font-size: 19px;
  }
  .card-front .brand-dot { width: 12px; height: 12px; }
  .holder {
    position: absolute;
    right: 56px; top: 52px;
    text-align: left;
    width: 178px;
  }
  .holder-name { font-size: 18px; font-weight: 700; }
  .holder-title { font-size: 13px; font-weight: 400; margin-top: 1px; }
  .contact {
    position: absolute;
    right: 40px; top: 160px;
    text-align: right;
    font-size: 13px;
    line-height: 21px;
  }
  .contact .address { margin-bottom: 22px; }
  .contact .label { font-weight: 700; }
  .card-back {
    left: 185px; top: 413px;
    width: 530px; height: 380px;
    background: var(--card-white);
  }
  .card-back .brand-name {
    left: 0; right: 0; top: 136px;
    justify-content: center;
    font-size: 28px;
  }
  .card-back .brand-dot { width: 16px; height: 16px; }
  .card-back .web {
    position: absolute;
    left: 0; right: 0; top: 286px;
    text-align: center;
    font-size: 12px;
    font-weight: 700;
    color: var(--brand-red);
  }
</style>
</head>
<body>
  <section class="card card-front">
    <svg class="white-swoop" width="540" height="420" viewBox="0 0 540 420" aria-hidden="true">
      <path d="M0,0 H252 C312,110 262,330 60,420 H0 Z" fill="var(--card-white)"/>
      <path d="M226,0 C286,110 236,320 0,410" fill="none" stroke="var(--curve-grey)" stroke-width="4"/>
    </svg>
    <div class="brand-name"><span class="brand-dot"></span>HARBOR KESTREL</div>
    <div class="holder">
      <p class="holder-name">Rosalind Okafor</p>
      <p class="holder-title">Partner</p>
    </div>
    <div class="contact">
      <p class="address">418 Tamarack Lane<br>Ashford Falls, OR 97402</p>
      <p><span class="label">Cell :</span> 503-555-0142</p>
      <p><span class="label">Email :</span> rosalind.okafor@harborkestrel.co</p>
      <p><span class="label">Web :</span> www.harborkestrel.co</p>
    </div>
  </section>

  <section class="card card-back">
    <div class="brand-name"><span class="brand-dot"></span>HARBOR KESTREL</div>
    <p class="web">www.harborkestrel.co</p>
  </section>
</body>
</html>
```